VPN Tech Comparison site. Clean and professional looking.

WORDPRESS

We need a website for "TunnelDesk" - A comparison website, news and article site.

We need a website that covers three main from top to bottom.

- Logo
- Menu underneath

- 5 Best of with a table of comparable features

then two columns, left column bigger, right column smaller

Right column to contain latest blog posts with thumbnails all the way down the same length as the left column.

Left column :

Separate section with each "Best for" in a separate section within.

- Best For Device ...

- Best for Country...

- Best for Features

Separate section with each "Latest" in a separate section within.

- Latest News

- Latest Reviews

- Latest Guides

- Latest Articles

Quite like the layout of http://www.vorbane.com/ so something along those lines, although not exactly and less graphically intense.

Target Market(s)

20-60 age range. Mostly male with some female.

Beginner friendly looking.

Industry/Entity Type

Information Technology

Number of Pages Required

2 page

Font styles to use
Sans Serif

Colors
32a6d6
33b8a4

Requirements
Must have
• 1 main page as described in the description.
• 1 blog post page with latest articles in a right side column.
Nice to have
• Easily readable font of a semi-big size for blog posts.
• Not overly graphical.

```html
<!DOCTYPE html>
<html lang="en">
<head>
<meta charset="utf-8">
<title>TunnelDesk – VPN Comparison, News and Guides</title>
<link rel="stylesheet" href="https://fonts.googleapis.com/css2?family=Lato:wght@400;700;900&family=Roboto+Slab:wght@400;700&family=Didact+Gothic&display=swap">
<style>
:root{
  --blue:#0a86c9;
  --blue-bright:#1c8fd6;
  --blue-dark:#0f56a8;
  --nav-active:#2b2b2b;
  --header-bg:#efefef;
  --page-bg:#e9e9e9;
  --text:#222;
  --muted:#666;
  --tile-bg:#e6f3fb;
  --tile-border:#bfe0f4;
  --star:#f7a21b;
  --table-bg:rgba(40,40,40,.88);
  --table-head:#4a4a4a;
  --white:#fff;
}
*{box-sizing:border-box;margin:0;padding:0}
html,body{width:1200px;height:2469px;overflow:hidden}
body{position:relative;background:var(--page-bg);font-family:'Lato',sans-serif;color:var(--text)}
.abs{position:absolute}

/* header */
.site-header{position:absolute;left:0;top:0;width:1200px;height:94px;background:var(--header-bg)}
.call-label{left:90px;top:16px;font-size:12px;font-weight:700;color:#333}
.call-number{left:90px;top:36px;font-size:20px;color:var(--blue);font-weight:400}
.brand{left:440px;top:18px;display:flex;align-items:center;gap:14px}
.brand-mark{width:44px;height:44px;border-radius:50%;background:var(--blue)}
.brand-name{font-size:40px;font-weight:700;color:var(--blue);letter-spacing:-.5px}
.follow-label{left:980px;top:16px;font-size:12px;font-weight:700;color:#333}
.social{left:980px;top:38px;display:flex;gap:16px}
.social span{width:30px;height:30px;border-radius:50%;border:3px solid var(--blue);display:block}

/* nav */
.main-nav{position:absolute;left:0;top:94px;width:1200px;height:44px;background:var(--blue)}
.main-nav ul{list-style:none;position:absolute;left:90px;top:0;display:flex;height:44px}
.main-nav li{height:44px;display:flex;align-items:center;justify-content:center;font-family:'Roboto Slab',serif;font-size:15px;color:var(--white);border-right:1px solid rgba(255,255,255,.25)}
.main-nav li.active{background:var(--nav-active);font-weight:700}

/* hero */
.hero{position:absolute;left:0;top:138px;width:1200px;height:446px;background:linear-gradient(100deg,#5a5a5a 0%,#3f3f3f 35%,#6b6b6b 70%,#3a3a3a 100%)}
.hero-photo{position:absolute;inset:0;background:radial-gradient(ellipse at 30% 40%,rgba(120,120,120,.5),transparent 60%)}
.hero-brand{left:90px;top:92px;display:flex;align-items:center;gap:14px}
.hero-brand .brand-mark{background:var(--white);width:52px;height:52px}
.hero-brand .brand-name{color:var(--white);font-size:42px}
.hero-title{left:90px;top:174px;width:400px;font-family:'Roboto Slab',serif;font-size:28px;line-height:38px;color:var(--white);letter-spacing:1px;text-transform:uppercase}
.hero-text{left:90px;top:262px;width:340px;font-size:14px;line-height:21px;color:#eee}
.btn-secure{left:90px;top:332px;width:152px;height:42px;background:var(--blue-bright);color:var(--white);font-family:'Roboto Slab',serif;font-size:16px;display:flex;align-items:center;justify-content:center}
.compare-title{left:494px;top:24px;width:617px;text-align:center;font-family:'Roboto Slab',serif;font-size:30px;color:var(--white);text-shadow:0 2px 4px rgba(0,0,0,.6)}
.compare-table{left:494px;top:84px;width:617px;border-collapse:collapse;background:var(--table-bg);color:var(--white);border-radius:4px;overflow:hidden}
.compare-table th{height:36px;background:var(--table-head);font-family:'Roboto Slab',serif;font-size:15px;font-weight:400;text-align:left;padding-left:12px}
.compare-table td{height:55px;border-top:1px solid #555;border-right:1px solid #555;vertical-align:middle;text-align:center}
.compare-table td:last-child{border-right:none}
.provider{text-align:left!important;padding-left:14px;font-weight:700;font-size:17px}
.price{font-size:19px;font-weight:700}
.loc b{display:block;font-size:19px}
.loc small{font-size:11px;color:#ccc}
.stars{color:var(--star);font-size:16px;letter-spacing:2px}
.buy{display:inline-block;width:78px;height:30px;line-height:30px;background:var(--blue-bright);font-size:12px;font-weight:700;border-radius:2px}

/* content card */
.content-card{position:absolute;left:69px;top:601px;width:1057px;height:1782px;background:var(--white);border-radius:8px;box-shadow:0 0 6px rgba(0,0,0,.25)}
.welcome{left:21px;top:24px;font-family:'Didact Gothic',sans-serif;font-size:34px;font-weight:400;color:#444}
.welcome b{font-family:'Roboto Slab',serif;font-weight:700;color:var(--blue-dark);font-size:32px;margin-left:8px}
.intro{left:21px;top:74px;width:725px;font-size:13px;line-height:20px;color:#111}
.find-bar{left:21px;top:209px;width:725px;height:36px;background:var(--blue-bright);border-radius:3px;color:var(--white);font-size:22px;padding-left:10px;line-height:36px}
.section-title{font-family:'Didact Gothic',sans-serif;font-weight:400;font-size:23px;color:#333;width:220px;border-bottom:1px solid #aaa;padding-bottom:6px}
.tile-row{display:flex;gap:22px}
.tile{width:160px;height:160px;background:var(--tile-bg);border:1px solid var(--tile-border);border-radius:4px;padding:8px}
.tile-img{height:118px;border-radius:3px}
.t1{background:linear-gradient(160deg,#7fd0ee,#1f7fb8)}
.t2{background:linear-gradient(160deg,#4a8ed0,#d8e8f2)}
.t3{background:linear-gradient(160deg,#0a1f5a,#2f74d0)}
.t4{background:linear-gradient(160deg,#0b2a6b,#5e8de0)}
.tile p{font-size:12px;text-align:center;margin-top:8px;color:#222;white-space:nowrap;letter-spacing:-.2px}
.tabs{left:21px;top:1287px;width:725px;height:42px;display:flex;border-bottom:3px solid var(--blue-bright)}
.tab{width:157px;height:39px;background:linear-gradient(#e4e4e4,#b9b9b9);font-family:'Roboto Slab',serif;font-size:15px;display:flex;align-items:center;justify-content:center;margin-right:2px;border-radius:3px 3px 0 0}
.tab.active{background:var(--blue-bright);color:var(--white);font-size:17px}
.news{width:343px}
.news-img{height:239px;border-radius:6px}
.n1{background:linear-gradient(150deg,#0b2f4a,#2fa7c9 55%,#0a1a2a)}
.n2{background:linear-gradient(150deg,#1c2e52,#5a90c8 55%,#0d3a82)}
.post-title{font-family:'Roboto Slab',serif;color:var(--blue-bright);font-size:20px;margin-top:22px}
.meta{font-size:13px;color:#555;margin-top:10px;display:flex;align-items:center;gap:6px;letter-spacing:.5px}
.meta b{color:#111;letter-spacing:0}
.news-text{font-size:13px;line-height:21px;margin-top:12px;font-weight:700;color:#111}
.news-text span{color:var(--blue-bright)}
.news-actions{margin-top:14px;padding-top:8px;border-top:1px solid #ddd;display:flex;gap:28px;font-size:12px;color:#444;width:300px}
.news-actions span{display:flex;align-items:center;gap:6px}
.side-post{position:absolute;left:777px;width:265px;border-bottom:1px solid #ddd;height:309px}
.side-img{height:177px;border-radius:3px}
.s1{background:linear-gradient(160deg,#eef2f6,#1d2b3c 60%,#7fb7e0)}
.s2{background:linear-gradient(160deg,#3a3f46,#8a7a60 50%,#1d2e4a)}
.s3{background:linear-gradient(160deg,#5da3cc,#0f2f56 60%,#c7d7e0)}
.s4{background:linear-gradient(160deg,#2a6c9a,#dfe6ec 50%,#143a5e)}
.side-post .post-title{margin-top:10px;font-size:19px}
.side-post .meta{margin-top:6px;font-size:12.5px}
.share{font-size:12px;color:#444;margin-top:10px;display:flex;align-items:center;gap:6px}

/* footer */
.site-footer{position:absolute;left:0;top:2421px;width:1200px;height:48px;background:var(--blue);color:var(--white);font-size:13px;text-align:center;line-height:48px}
</style>
</head>
<body>

<header class="site-header">
  <div class="abs call-label">CALL US:</div>
  <div class="abs call-number">123-456-7890</div>
  <div class="abs brand"><span class="brand-mark"></span><span class="brand-name">TunnelDesk</span></div>
  <div class="abs follow-label">FOLLOW US:</div>
  <div class="abs social" aria-label="Social links"><span></span><span></span><span></span></div>
</header>

<nav class="main-nav">
  <ul>
    <li class="active" style="width:132px">Home</li>
    <li style="width:157px">About Us</li>
    <li style="width:131px">News</li>
    <li style="width:140px">Articles</li>
    <li style="width:150px">Reviews</li>
    <li style="width:140px">Guides</li>
    <li style="width:168px">Contact Us</li>
  </ul>
</nav>

<section class="hero">
  <div class="hero-photo" role="img" aria-label="Photo of an office desk with computer monitors"></div>
  <div class="abs hero-brand"><span class="brand-mark"></span><span class="brand-name">TunnelDesk</span></div>
  <h1 class="abs hero-title">Provides an extra layer of security</h1>
  <p class="abs hero-text">Individuals Can Remotely Access A Protected Network From Any Internet Connection.</p>
  <div class="abs btn-secure">GET SECURED</div>

  <h2 class="abs compare-title">TOP 5 VPN Providers Comparison</h2>
  <table class="abs compare-table">
    <thead><tr><th style="width:148px">VPN Provider</th><th style="width:104px">Monthly</th><th style="width:110px">Locations</th><th style="width:140px">User Rating</th><th></th></tr></thead>
    <tbody>
      <tr><td class="provider">SwiftLane</td><td class="price">$ 8.32</td><td class="loc"><b>78</b><small>Countries</small></td><td class="stars">★★★★★</td><td><span class="buy">BUY IT!</span></td></tr>
      <tr><td class="provider">Harborly</td><td class="price">$ 4.01</td><td class="loc"><b>24</b><small>Countries</small></td><td class="stars">★★★★★</td><td><span class="buy">BUY IT!</span></td></tr>
      <tr><td class="provider">CloakNest</td><td class="price">$ 5.99</td><td class="loc"><b>182</b><small>Countries</small></td><td class="stars">★★★★★</td><td><span class="buy">BUY IT!</span></td></tr>
      <tr><td class="provider">Veilpath</td><td class="price">$ 6.49</td><td class="loc"><b>61</b><small>Countries</small></td><td class="stars">★★★★★</td><td><span class="buy">BUY IT!</span></td></tr>
      <tr><td class="provider">Lumora</td><td class="price">$ 3.75</td><td class="loc"><b>120</b><small>Countries</small></td><td class="stars">★★★★★</td><td><span class="buy">BUY IT!</span></td></tr>
    </tbody>
  </table>
</section>

<main class="content-card">
  <h2 class="abs welcome">Welcome to<b>TUNNELDESK</b></h2>
  <p class="abs intro">Lorem ipsum dolor sit amet, sed diam nonummy nibh euismod tincidunt ut laoreet dolore magna aliquam erat volutpat. Ut wisi enim ad minim veniam, quis nostrud exerci tation ullamcorper suscipit lobortis nisl ut aliquip ex ea commodo consequat. Duis autem vel eum iriure dolor in hendrerit in vulputate velit esse molestie consequat, vel illum dolore eu feugiat nulla facilisis at vero eros et accumsan et iusto odio dignissim qui blandit praesent luptatum zzril delenit augue duis dolore te feugait nulla facilisi.</p>
  <div class="abs find-bar">Find the Best VPN for...</div>

  <section class="abs" style="left:21px;top:253px">
    <h3 class="section-title">Best VPN for Device</h3>
    <div class="tile-row" style="margin-top:16px;margin-left:9px">
      <div class="tile"><div class="tile-img t1" role="img" aria-label="Globe with connected computers"></div><p>Best VPN for Nimbix</p></div>
      <div class="tile"><div class="tile-img t2" role="img" aria-label="Woman touching a digital screen"></div><p>Best VPN for Corvo</p></div>
      <div class="tile"><div class="tile-img t3" role="img" aria-label="Glowing fibre optic lines"></div><p>Best VPN for Tessel</p></div>
      <div class="tile"><div class="tile-img t4" role="img" aria-label="Blue digital data grid"></div><p>Best VPN for Quartzo</p></div>
    </div>
  </section>

  <section class="abs" style="left:21px;top:508px">
    <h3 class="section-title">Best VPN for Country</h3>
    <div class="tile-row" style="margin-top:18px;margin-left:9px">
      <div class="tile"><div class="tile-img t1" role="img" aria-label="Globe with connected computers"></div><p>Best VPN for USA</p></div>
      <div class="tile"><div class="tile-img t2" role="img" aria-label="Woman touching a digital screen"></div><p>Best VPN for China</p></div>
      <div class="tile"><div class="tile-img t3" role="img" aria-label="Glowing fibre optic lines"></div><p>Best VPN for Australia</p></div>
      <div class="tile"><div class="tile-img t4" role="img" aria-label="Blue digital data grid"></div><p>Best VPN for UK</p></div>
    </div>
  </section>

  <section class="abs" style="left:21px;top:765px">
    <h3 class="section-title">Best VPN for Features</h3>
    <div class="tile-row" style="margin-top:18px;margin-left:9px">
      <div class="tile"><div class="tile-img t1" role="img" aria-label="Globe with connected computers"></div><p>Best VPN for Torrents</p></div>
      <div class="tile"><div class="tile-img t2" role="img" aria-label="Woman touching a digital screen"></div><p>Best VPN for Gaming</p></div>
      <div class="tile"><div class="tile-img t3" role="img" aria-label="Glowing fibre optic lines"></div><p>Best VPN for TV Services</p></div>
      <div class="tile"><div class="tile-img t4" role="img" aria-label="Blue digital data grid"></div><p>Best No Log VPN provider</p></div>
    </div>
  </section>

  <section class="abs" style="left:19px;top:1023px">
    <h3 class="section-title">Best for Entertainment</h3>
    <div class="tile-row" style="margin-top:18px;margin-left:11px">
      <div class="tile"><div class="tile-img t1" role="img" aria-label="Globe with connected computers"></div><p>Best VPN for Telvio Play</p></div>
      <div class="tile"><div class="tile-img t2" role="img" aria-label="Woman touching a digital screen"></div><p>Best VPN for Streamora</p></div>
      <div class="tile"><div class="tile-img t3" role="img" aria-label="Glowing fibre optic lines"></div><p>Best VPN for Vidlane</p></div>
      <div class="tile"><div class="tile-img t4" role="img" aria-label="Blue digital data grid"></div><p>Best VPN for Vidlane</p></div>
    </div>
  </section>

  <div class="abs tabs">
    <div class="tab active">Latest News</div>
    <div class="tab">Latest Reviews</div>
    <div class="tab">Latest Guides</div>
    <div class="tab">Latest Articles</div>
  </div>

  <article class="abs news" style="left:21px;top:1349px">
    <div class="news-img n1" role="img" aria-label="Close-up of a glowing circuit board chip"></div>
    <h4 class="post-title">Lorem Ipsum Dolor Sit</h4>
    <div class="meta"><svg width="12" height="12" viewBox="0 0 12 12"><circle cx="6" cy="6" r="5" fill="none" stroke="#1c8fd6" stroke-width="1.5"/><path d="M6 3v3l2 1" stroke="#1c8fd6" stroke-width="1.5" fill="none"/></svg>DEC 18, 2015 &nbsp;|&nbsp; BY <b>Lorem Ipsum</b></div>
    <p class="news-text">Lorem ipsum dolor sit amet, sed diam nonummy nibh euismod tincidunt ut laoreet dolore magna <span>[...]</span></p>
    <div class="news-actions"><span><svg width="12" height="11" viewBox="0 0 12 11"><path d="M1 1h10v6H5l-3 3V7H1z" fill="#1c8fd6"/></svg>Leave A Comment</span><span><svg width="12" height="11" viewBox="0 0 12 11"><path d="M1 5h2v6H1zM4 5l3-5c1 0 2 1 1 3h3v3l-2 5H4z" fill="#1c8fd6"/></svg>Like Us</span><span><svg width="12" height="12" viewBox="0 0 12 12"><circle cx="9" cy="2.5" r="2" fill="#1c8fd6"/><circle cx="3" cy="6" r="2" fill="#1c8fd6"/><circle cx="9" cy="9.5" r="2" fill="#1c8fd6"/><path d="M9 2.5L3 6l6 3.5" stroke="#1c8fd6" fill="none"/></svg>Share</span></div>
  </article>

  <article class="abs news" style="left:403px;top:1349px">
    <div class="news-img n2" role="img" aria-label="Server racks beside a blue globe"></div>
    <h4 class="post-title">Lorem Ipsum Dolor Sit</h4>
    <div class="meta"><svg width="12" height="12" viewBox="0 0 12 12"><circle cx="6" cy="6" r="5" fill="none" stroke="#1c8fd6" stroke-width="1.5"/><path d="M6 3v3l2 1" stroke="#1c8fd6" stroke-width="1.5" fill="none"/></svg>DEC 18, 2015 &nbsp;|&nbsp; BY <b>Lorem Ipsum</b></div>
    <p class="news-text">Lorem ipsum dolor sit amet, sed diam nonummy nibh euismod tincidunt ut laoreet dolore magna <span>[...]</span></p>
    <div class="news-actions"><span><svg width="12" height="11" viewBox="0 0 12 11"><path d="M1 1h10v6H5l-3 3V7H1z" fill="#1c8fd6"/></svg>Leave A Comment</span><span><svg width="12" height="11" viewBox="0 0 12 11"><path d="M1 5h2v6H1zM4 5l3-5c1 0 2 1 1 3h3v3l-2 5H4z" fill="#1c8fd6"/></svg>Like Us</span><span><svg width="12" height="12" viewBox="0 0 12 12"><circle cx="9" cy="2.5" r="2" fill="#1c8fd6"/><circle cx="3" cy="6" r="2" fill="#1c8fd6"/><circle cx="9" cy="9.5" r="2" fill="#1c8fd6"/><path d="M9 2.5L3 6l6 3.5" stroke="#1c8fd6" fill="none"/></svg>Share</span></div>
  </article>

  <aside>
    <article class="side-post" style="top:33px">
      <div class="side-img s1" role="img" aria-label="Hands holding a tablet with network graphics"></div>
      <h4 class="post-title">Lorem Ipsum Dolor Sit</h4>
      <div class="meta"><svg width="12" height="12" viewBox="0 0 12 12"><circle cx="6" cy="6" r="5" fill="none" stroke="#1c8fd6" stroke-width="1.5"/><path d="M6 3v3l2 1" stroke="#1c8fd6" stroke-width="1.5" fill="none"/></svg>DEC 18, 2015 &nbsp;|&nbsp; BY <b>Lorem Ipsum</b></div>
      <div class="share"><svg width="12" height="12" viewBox="0 0 12 12"><circle cx="9" cy="2.5" r="2" fill="#1c8fd6"/><circle cx="3" cy="6" r="2" fill="#1c8fd6"/><circle cx="9" cy="9.5" r="2" fill="#1c8fd6"/><path d="M9 2.5L3 6l6 3.5" stroke="#1c8fd6" fill="none"/></svg>Share</div>
    </article>
    <article class="side-post" style="top:342px">
      <div class="side-img s2" role="img" aria-label="Technician working at a server cabinet"></div>
      <h4 class="post-title">Lorem Ipsum Dolor Sit</h4>
      <div class="meta"><svg width="12" height="12" viewBox="0 0 12 12"><circle cx="6" cy="6" r="5" fill="none" stroke="#1c8fd6" stroke-width="1.5"/><path d="M6 3v3l2 1" stroke="#1c8fd6" stroke-width="1.5" fill="none"/></svg>DEC 18, 2015 &nbsp;|&nbsp; BY <b>Lorem Ipsum</b></div>
      <div class="share"><svg width="12" height="12" viewBox="0 0 12 12"><circle cx="9" cy="2.5" r="2" fill="#1c8fd6"/><circle cx="3" cy="6" r="2" fill="#1c8fd6"/><circle cx="9" cy="9.5" r="2" fill="#1c8fd6"/><path d="M9 2.5L3 6l6 3.5" stroke="#1c8fd6" fill="none"/></svg>Share</div>
    </article>
    <article class="side-post" style="top:651px">
      <div class="side-img s3" role="img" aria-label="Close-up of a blue circuit board"></div>
      <h4 class="post-title">Lorem Ipsum Dolor Sit</h4>
      <div class="meta"><svg width="12" height="12" viewBox="0 0 12 12"><circle cx="6" cy="6" r="5" fill="none" stroke="#1c8fd6" stroke-width="1.5"/><path d="M6 3v3l2 1" stroke="#1c8fd6" stroke-width="1.5" fill="none"/></svg>DEC 18, 2015 &nbsp;|&nbsp; BY <b>Lorem Ipsum</b></div>
      <div class="share"><svg width="12" height="12" viewBox="0 0 12 12"><circle cx="9" cy="2.5" r="2" fill="#1c8fd6"/><circle cx="3" cy="6" r="2" fill="#1c8fd6"/><circle cx="9" cy="9.5" r="2" fill="#1c8fd6"/><path d="M9 2.5L3 6l6 3.5" stroke="#1c8fd6" fill="none"/></svg>Share</div>
    </article>
    <article class="side-post" style="top:960px">
      <div class="side-img s4" role="img" aria-label="Engineer standing in a data centre"></div>
      <h4 class="post-title">Lorem Ipsum Dolor Sit</h4>
      <div class="meta"><svg width="12" height="12" viewBox="0 0 12 12"><circle cx="6" cy="6" r="5" fill="none" stroke="#1c8fd6" stroke-width="1.5"/><path d="M6 3v3l2 1" stroke="#1c8fd6" stroke-width="1.5" fill="none"/></svg>DEC 18, 2015 &nbsp;|&nbsp; BY <b>Lorem Ipsum</b></div>
      <div class="share"><svg width="12" height="12" viewBox="0 0 12 12"><circle cx="9" cy="2.5" r="2" fill="#1c8fd6"/><circle cx="3" cy="6" r="2" fill="#1c8fd6"/><circle cx="9" cy="9.5" r="2" fill="#1c8fd6"/><path d="M9 2.5L3 6l6 3.5" stroke="#1c8fd6" fill="none"/></svg>Share</div>
    </article>
    <article class="side-post" style="top:1269px">
      <div class="side-img s1" role="img" aria-label="Hands holding a tablet with network graphics"></div>
      <h4 class="post-title">Lorem Ipsum Dolor Sit</h4>
      <div class="meta"><svg width="12" height="12" viewBox="0 0 12 12"><circle cx="6" cy="6" r="5" fill="none" stroke="#1c8fd6" stroke-width="1.5"/><path d="M6 3v3l2 1" stroke="#1c8fd6" stroke-width="1.5" fill="none"/></svg>DEC 18, 2015 &nbsp;|&nbsp; BY <b>Lorem Ipsum</b></div>
      <div class="share"><svg width="12" height="12" viewBox="0 0 12 12"><circle cx="9" cy="2.5" r="2" fill="#1c8fd6"/><circle cx="3" cy="6" r="2" fill="#1c8fd6"/><circle cx="9" cy="9.5" r="2" fill="#1c8fd6"/><path d="M9 2.5L3 6l6 3.5" stroke="#1c8fd6" fill="none"/></svg>Share</div>
    </article>
  </aside>
</main>

<footer class="site-footer">Copyright 2015 TunnelDesk. All Rights Reserved.</footer>

</body>
</html>
```